PelvoStudio Brochure Design - UPDATE/BUDGET INCREASE

Thanks everyone that have submitted designes. Please see the updates below (mostly the pricing guide and information).

UPDATE:

All images that should be used are located here: https://www.filecrate.example/sh/kq7trmwpzbex04u/Vb8xRt2LpN

Brochure needed to showcase photography and videography prices for potential brides and couples engaged to be married. The brochure should have 5 -6 sections that shows the various wedding media service packages we offer. We will provide the information in tiers for you to lay it out creatively.

We are looking for a half-fold 11x17 that we can place inside of "swag bags" at the smaller bridal shows. Die cut options are a plus.

We need our affiliations and credentials above the PelvoStudio Logo on the front of the brochure.

Our contact information is needed at the bottom on the front of the brochure to read:

"Contact us today | info@pelvostudio.org | 414.286.7302"
www.pelvostudiophotography.com
available worldwide

The inside should have the information containing the photography and videography prices. The outside will contain images and a logo that we will provide for you.

Lastly, we need information about our organization. Please incorporate the information located on the brochure in the filecrate folder provided above.

PRICING UPDATE:

MATINEE - $995
4 Hour Photography Service
2 Digital Enhancements on Signature Images
500 Hi-Res Images on Laser Engraved DVD
Cataloged and Sequenced by Event Sequence
Photo Release

FULL FEATURE - $1595
5 Hour Photography Service
20 - Page LayFlat PhotoBook
1 Custom Graphic Creation
5 Digital Enhancements on Signature Images
800 Hi-Res Images on Laser Engraved DVD
Photo Release

DOUBLE FEATURE - $1899
6 Hour Photography Service
1 Additional Photo Session
1 Custom Graphic Creation
1000 Hi-Res Images on Laser Engraved DVD
Photo Release

BLOCKBUSTER - $2199
7 Hour Photography Service
1 Custom Graphic Creation
1200 Hi-Res Images on Laser Engraved DVD
Photo Release

DIRECTORS CUT - $2499
8 Hour Photography Service
1 Custom Graphic Creation
10 Digital Enhancements on Signature Images
1400 Hi-Res Images on Laser Engraved DVD
Photo Release

VIDEO - BONUS REEL - $1795 (this should be a distinct section that clearly speaks video).
6 Hour Video Service
7 - 10 min Cinematic Highlight Reel
Full Ceremony Chapter optional
Royalty Free Soundtrack
Optimization for Online Upload
2 DVD's on Laser Engraved Disks
Online Hosting for 2 month

Target Market(s)

Brides and couples engaged to be married

Industry/Entity Type

Digital

Requirements
Must have
• https://www.filecrate.example/sh/4tbw82jrnq5ym0c/HzYe6WmDkS for images that we would like in the design.

Nice to have
• designed to take advantage of die cut printers

```html
<!DOCTYPE html>
<html lang="en">
<head>
<meta charset="utf-8">
<title>PelvoStudio Wedding Packages Brochure – Inside Spread</title>
<link rel="stylesheet" href="https://fonts.googleapis.com/css2?family=Montserrat:wght@400;500;700;800&family=Great+Vibes&display=swap">
<style>
  :root{
    --canvas:#3a3a3a;
    --page-top:#e9e6ea;
    --page-mid:#d9d2d8;
    --page-low:#cfc6cc;
    --frame:#c8bca6;
    --frame-edge:#b3a68e;
    --clip:#cdbf95;
    --clip-edge:#a8996c;
    --matinee:#f57f8f;
    --full:#0f9a9e;
    --double:#3a9f57;
    --block:#f38a3c;
    --director:#9aa03a;
    --video:#2f69a5;
    --ink-light:#ffffff;
    --logo-ink:#3b3b3b;
    --script:rgba(120,110,120,.28);
    --photo-dark:#1d1d20;
    --photo-mid:#4a3f3c;
    --pin:#d6262a;
  }
  *{box-sizing:border-box;margin:0;padding:0}
  html,body{width:1200px;height:1000px;overflow:hidden}
  body{background:var(--canvas);font-family:"Montserrat",sans-serif;position:relative}

  .spread{position:absolute;left:90px;top:120px;width:1020px;height:760px;display:flex;box-shadow:0 20px 40px rgba(0,0,0,.45)}
  .page{position:relative;width:510px;height:760px;overflow:hidden}
  .page-backdrop{position:absolute;inset:0;background:linear-gradient(160deg,var(--page-top) 0%,var(--page-mid) 45%,var(--page-low) 100%)}
  .page--right .page-backdrop{background:linear-gradient(200deg,var(--page-top) 0%,var(--page-mid) 50%,var(--page-low) 100%)}
  .fold{position:absolute;left:509px;top:0;width:2px;height:760px;background:rgba(0,0,0,.12)}

  .script-mark{position:absolute;font-family:"Great Vibes",cursive;font-size:96px;color:var(--script);white-space:nowrap;pointer-events:none}
  .script-mark--upper{left:300px;top:20px;transform:rotate(28deg);transform-origin:left top}
  .script-mark--lower{left:70px;top:620px;transform:rotate(18deg);transform-origin:left top}

  .card{position:absolute;background:var(--frame);padding:10px 10px 26px;box-shadow:4px 6px 10px rgba(0,0,0,.35);border:1px solid var(--frame-edge)}
  .card-clip{position:absolute;top:-22px;left:50%;width:14px;height:46px;margin-left:-7px;background:var(--clip);border:1px solid var(--clip-edge);border-radius:2px}
  .card-clip::after{content:"";position:absolute;left:5px;top:4px;width:2px;height:36px;background:var(--clip-edge)}
  .card-panel{color:var(--ink-light);padding:12px 12px}
  .card-title{font-weight:800;font-size:13px;letter-spacing:.2px;text-transform:uppercase;margin-bottom:5px;line-height:1.2}
  .card-title .price{font-size:16px;white-space:nowrap}
  .card-note{font-size:7px;font-style:italic;margin-bottom:3px;line-height:1.25}
  .card-list{list-style:none;font-size:8.5px;line-height:1.35;font-weight:500}

  .card--matinee{left:40px;top:40px;width:265px;transform:rotate(6deg)}
  .card--matinee .card-panel{background:var(--matinee)}
  .card--full{left:240px;top:215px;width:255px;transform:rotate(8deg)}
  .card--full .card-panel{background:var(--full)}
  .card--double{left:18px;top:370px;width:262px;transform:rotate(7deg)}
  .card--double .card-panel{background:var(--double)}
  .card--block{left:240px;top:530px;width:255px;transform:rotate(6deg)}
  .card--block .card-panel{background:var(--block)}
  .card--director{left:14px;top:450px;width:232px;transform:rotate(-5deg)}
  .card--director .card-panel{background:var(--director)}
  .card--video{left:252px;top:440px;width:246px;transform:rotate(2deg)}
  .card--video .card-panel{background:var(--video)}

  .brand{position:absolute;left:30px;top:700px;display:flex;align-items:center;gap:10px}
  .brand-dot{width:12px;height:12px;border-radius:50%;background:var(--logo-ink)}
  .brand-name{font-family:"Montserrat",sans-serif;font-weight:500;font-size:26px;color:var(--logo-ink);letter-spacing:1px}

  .feature-photo{position:absolute;left:45px;top:80px;width:420px;height:290px;background:#fff;padding:12px;box-shadow:5px 8px 14px rgba(0,0,0,.4);transform:rotate(2deg)}
  .feature-photo-fill{width:100%;height:100%;background:linear-gradient(135deg,var(--photo-dark) 0%,var(--photo-mid) 55%,#8a7d78 100%)}
  .feature-pin{position:absolute;left:185px;top:-24px}
</style>
</head>
<body>
  <section class="spread" aria-label="Brochure inside spread">
    <article class="page page--left">
      <div class="page-backdrop" role="img" aria-label="Soft close-up of a couple's hands with wedding rings"></div>
      <span class="script-mark script-mark--upper">Photography</span>

      <div class="card card--matinee">
        <span class="card-clip"></span>
        <div class="card-panel">
          <h2 class="card-title">Matinee - <span class="price">$995</span></h2>
          <ul class="card-list">
            <li>4 Hour Photography Service</li>
            <li>2 Digital Enhancements on Signature Images</li>
            <li>500 Hi-Res Images on Laser Engraved DVD</li>
            <li>Cataloged and Sequenced by Event Sequence</li>
            <li>Photo Release</li>
          </ul>
        </div>
      </div>

      <div class="card card--full">
        <span class="card-clip"></span>
        <div class="card-panel">
          <h2 class="card-title">Full Feature - <span class="price">$1595</span></h2>
          <ul class="card-list">
            <li>5 Hour Photography Service</li>
            <li>20 - Page LayFlat PhotoBook</li>
            <li>1 Custom Graphic Creation</li>
            <li>5 Digital Enhancements on Signature Images</li>
            <li>800 Hi-Res Images on Laser Engraved DVD</li>
            <li>Photo Release</li>
          </ul>
        </div>
      </div>

      <div class="card card--double">
        <span class="card-clip"></span>
        <div class="card-panel">
          <h2 class="card-title">Double Feature - <span class="price">$1899</span></h2>
          <ul class="card-list">
            <li>6 Hour Photography Service</li>
            <li>1 Additional Photo Session</li>
            <li>1 Custom Graphic Creation</li>
            <li>1000 Hi-Res Images on Laser Engraved DVD</li>
            <li>Photo Release</li>
          </ul>
        </div>
      </div>

      <div class="card card--block">
        <span class="card-clip"></span>
        <div class="card-panel">
          <h2 class="card-title">Blockbuster - <span class="price">$2199</span></h2>
          <ul class="card-list">
            <li>7 Hour Photography Service</li>
            <li>1 Custom Graphic Creation</li>
            <li>1200 Hi-Res Images on Laser Engraved DVD</li>
            <li>Photo Release</li>
          </ul>
        </div>
      </div>

      <div class="brand">
        <span class="brand-dot"></span>
        <span class="brand-name">PelvoStudio</span>
      </div>
    </article>

    <article class="page page--right">
      <div class="page-backdrop" role="img" aria-label="Soft close-up of a couple's hands with wedding rings"></div>
      <span class="script-mark script-mark--lower">Photography</span>

      <figure class="feature-photo">
        <div class="feature-photo-fill" role="img" aria-label="Wedding guests celebrating with drinks at a bar"></div>
        <svg class="feature-pin" width="40" height="48" viewBox="0 0 40 48" aria-hidden="true">
          <line x1="14" y1="30" x2="4" y2="46" stroke="#888" stroke-width="2"/>
          <ellipse cx="22" cy="26" rx="12" ry="5" fill="var(--pin)"/>
          <rect x="17" y="10" width="10" height="16" rx="2" fill="var(--pin)"/>
          <ellipse cx="22" cy="9" rx="9" ry="4" fill="#e8474a"/>
        </svg>
      </figure>

      <div class="card card--director">
        <span class="card-clip"></span>
        <div class="card-panel">
          <h2 class="card-title">Directors Cut - <span class="price">$2499</span></h2>
          <ul class="card-list">
            <li>8 Hour Photography Service</li>
            <li>1 Custom Graphic Creation</li>
            <li>10 Digital Enhancements on Signature Images</li>
            <li>1400 Hi-Res Images on Laser Engraved DVD</li>
            <li>Photo Release</li>
          </ul>
        </div>
      </div>

      <div class="card card--video">
        <span class="card-clip"></span>
        <div class="card-panel">
          <h2 class="card-title">Video - Bonus Reel - <span class="price">$1795</span></h2>
          <p class="card-note">(this should be a distinct section that clearly speaks video).</p>
          <ul class="card-list">
            <li>6 Hour Video Service</li>
            <li>7 - 10 min Cinematic Highlight Reel</li>
            <li>Full Ceremony Chapter optional</li>
            <li>Royalty Free Soundtrack</li>
            <li>Optimization for Online Upload</li>
            <li>2 DVD's on Laser Engraved Disks</li>
            <li>Online Hosting for 2 month</li>
          </ul>
        </div>
      </div>
    </article>
    <span class="fold"></span>
  </section>
</body>
</html>
```